VantoMedix website

I have a plumfield hosting website already & have been using wordpress.
See www.vantomedix-sample.com
I have a logo's already.
I need a front page "VantoMedix". I have 3 products: (need separate pages)
1) the "GlideTray" (can't supply images ATM)
2) the "TubeKeeper" (several stills below & animation: http://www.clipvault-example.com/watch?v=Z7HqR20mW3x&list=QPtr8B_kzoepWnXcM4Lq5B_T&feature=share)
3) the "FastPart" animation here: http://clipv.example/pwrtk-Mmo_E & logo as below

It needs to be corporate & professional looking. VantoMedix is an innovative design house for medical devices.

Reason: Hi Designers, thanks for all your work to date - there have been some great designs. We'll be providing feedback to some of you in the near future. The reason we have extended the deadline is simply that we are too busy with other aspects of the business to focus on this at the moment. Kind regards, the VantoMedix team.

Dear Designers,

VantoMedix apologies for the delay due to our busyness. 
Please help us to understand the process here:
are we getting fully working websites? With multiple pages? Will we be able to modify them?
If not, what is the output?

Kind regards,
the Vanto team.

```html
<!DOCTYPE html>
<html lang="en">
<head>
<meta charset="utf-8">
<title>VantoMedix</title>
<link href="https://fonts.googleapis.com/css2?family=Open+Sans:wght@300;400;600&family=Titillium+Web:wght@300;400;700&display=swap" rel="stylesheet">
<style>
  :root {
    --brand-blue: #2aa3dc;
    --brand-orange: #f26b12;
    --deep-blue: #0a4867;
    --deep-blue-light: #14607f;
    --hero-dark: #2f6f91;
    --hero-light: #69a8cf;
    --text-dark: #2b2b2b;
    --text-body: #6b6b6b;
    --rule: #cfcfcf;
    --white: #ffffff;
    --button-dark: #3a3a3a;
  }
  * { box-sizing: border-box; margin: 0; padding: 0; }
  html, body { width: 859px; height: 1200px; overflow: hidden; }
  body { font-family: "Open Sans", Arial, sans-serif; background: var(--white); color: var(--text-dark); position: relative; }

  .site-header { height: 40px; display: flex; align-items: center; justify-content: space-between; padding: 0 118px 0 114px; background: var(--white); }
  .brand { display: flex; align-items: center; gap: 5px; font-family: "Titillium Web", sans-serif; font-weight: 700; font-size: 21px; color: var(--brand-blue); letter-spacing: -0.2px; }
  .brand-dot { width: 12px; height: 12px; border-radius: 50%; background: var(--brand-orange); }
  .main-nav { display: flex; gap: 33px; font-size: 10px; text-transform: uppercase; }
  .main-nav a { color: var(--text-dark); text-decoration: none; }
  .main-nav a.is-active { color: var(--brand-orange); }

  .hero { position: relative; height: 381px; overflow: hidden; }
  .hero-media { position: absolute; inset: 0; background: radial-gradient(ellipse at 55% 40%, var(--hero-light) 0%, #4f8fb8 40%, var(--hero-dark) 100%); }
  .hero-title { position: absolute; left: 134px; top: 98px; width: 581px; height: 64px; background: rgba(255,255,255,0.22); border: 3px solid rgba(255,255,255,0.18); display: flex; align-items: center; justify-content: center; font-family: "Titillium Web", sans-serif; font-weight: 300; font-size: 36px; color: var(--white); letter-spacing: 0.5px; }
  .hero-title strong { font-weight: 700; }
  .hero-play { position: absolute; left: 407px; top: 198px; }
  .hero-dots { position: absolute; left: 366px; top: 363px; display: flex; gap: 4px; }
  .hero-dots span { width: 38px; height: 4px; background: var(--white); border-radius: 1px; }
  .hero-dots span.is-current { background: var(--brand-orange); }

  .section-title { text-align: center; font-weight: 300; font-size: 26px; letter-spacing: 0.3px; }
  .title-rule { position: relative; width: 128px; height: 1px; margin: 5px auto 0; background: var(--rule); }
  .title-rule::after { content: ""; position: absolute; left: 61px; top: -3px; width: 5px; height: 5px; background: var(--brand-orange); transform: rotate(45deg); }

  .welcome { height: 279px; padding-top: 32px; text-align: center; }
  .welcome-text { width: 622px; margin: 20px auto 0; font-size: 9.6px; line-height: 19px; color: var(--text-body); }
  .button-outline { display: inline-block; margin-top: 24px; width: 115px; height: 32px; line-height: 30px; border: 1px solid var(--text-dark); border-radius: 2px; font-size: 12.5px; color: var(--text-dark); text-decoration: none; }

  .products { position: relative; height: 500px; padding-top: 33px; color: var(--white); }
  .products-backdrop { position: absolute; inset: 0; background: linear-gradient(160deg, var(--deep-blue-light) 0%, var(--deep-blue) 45%, #0a4565 100%); }
  .products .section-title { position: relative; color: var(--white); font-size: 32px; }
  .products .title-rule { position: relative; background: rgba(255,255,255,0.35); }
  .product-grid { position: relative; display: flex; gap: 15px; width: 622px; margin: 29px auto 0; }
  .product-card { width: 198px; height: 306px; background: var(--white); border-radius: 2px; text-align: center; padding-top: 27px; }
  .product-icon { display: block; margin: 0 auto; }
  .product-name { margin-top: 10px; font-family: "Titillium Web", sans-serif; font-size: 16px; font-weight: 400; }
  .product-name.is-blue { color: var(--brand-blue); }
  .product-name.is-teal { color: #1f8bc7; }
  .product-name.is-orange { color: var(--brand-orange); }
  .product-name .accent { color: var(--brand-orange); }
  .product-text { margin: 5px auto 0; width: 182px; font-size: 7.4px; line-height: 15.5px; color: var(--text-body); }
  .button-solid { display: inline-block; margin-top: 17px; width: 70px; height: 23px; line-height: 21px; border: 1px solid #222; border-radius: 2px; background: var(--button-dark); color: var(--white); font-size: 8.5px; text-decoration: none; }
  .button-solid.is-orange { background: var(--brand-orange); border-color: #d8540a; }
</style>
</head>
<body>
  <header class="site-header">
    <div class="brand"><span class="brand-name">VantoMedix</span><span class="brand-dot"></span></div>
    <nav class="main-nav">
      <a class="is-active" href="#">Home</a>
      <a href="#">About</a>
      <a href="#">Ask a Question</a>
      <a href="#">Contact Us</a>
    </nav>
  </header>

  <section class="hero">
    <div class="hero-media" role="img" aria-label="Blurred close-up photograph of a blue medical tubing device"></div>
    <h1 class="hero-title">HELPING&nbsp;<strong>YOU</strong>,LIVE YOUR&nbsp;<strong>LIFE</strong></h1>
    <svg class="hero-play" width="70" height="70" viewBox="0 0 70 70" aria-label="Play video">
      <circle cx="35" cy="35" r="32.5" fill="none" stroke="rgba(255,255,255,0.75)" stroke-width="3"/>
      <path d="M28 22 L47 35 L28 48 Z" fill="none" stroke="rgba(255,255,255,0.75)" stroke-width="3" stroke-linejoin="round"/>
    </svg>
    <div class="hero-dots"><span></span><span class="is-current"></span><span></span></div>
  </section>

  <section class="welcome">
    <h2 class="section-title">WELCOME TO</h2>
    <div class="title-rule"></div>
    <p class="welcome-text">Lorem ipsum dolor sit amet, consectetur adipiscing elit. Nunc eget nunc vitae tellus luctus ullamcorper. Nam porttitor ullamcorper felis at convallis. Aenean ornare vestibulum nisi fringilla lacinia. Nullam pulvinar sollicitudin velit id laoreet. Quisque non rhoncus sem.Nullam vinar sollicitudin velit id laoreet.Lorem ipsum dolor sit amet, consectetur adipiscing elit. Nunc eget nunc vitae tellus luctus ullamcorper. Namttitor ullamcorper felis at convallis. Aenean ornare vestibulum nisi fringilla lacinia. Nullam pulvinar sollicitudin velit id laoreet. Quisque non rhoncus sem.Nullam pulvinar sollicitudin velit id laoreet</p>
    <a class="button-outline" href="#">LEARN MORE</a>
  </section>

  <section class="products">
    <div class="products-backdrop" role="img" aria-label="Deep blue background with soft flowing light waves"></div>
    <h2 class="section-title">PRODUCTS</h2>
    <div class="title-rule"></div>
    <div class="product-grid">
      <article class="product-card">
        <svg class="product-icon" width="112" height="112" viewBox="0 0 112 112" aria-hidden="true">
          <circle cx="56" cy="56" r="56" fill="#2aa8e0"/>
          <circle cx="56" cy="56" r="36" fill="none" stroke="#fff" stroke-width="3"/>
          <circle cx="56" cy="56" r="32" fill="#fff"/>
          <path d="M41 72 L68 45" stroke="var(--brand-orange)" stroke-width="7" stroke-linecap="round"/>
          <path d="M43 42 l2 -5 l2 5 l5 2 l-5 2 l-2 5 l-2 -5 l-5 -2 z M56 38 l1 -3 l1 3 l3 1 l-3 1 l-1 3 l-1 -3 l-3 -1 z M38 53 l1 -2 l1 2 l2 1 l-2 1 l-1 2 l-1 -2 l-2 -1 z" fill="var(--brand-orange)"/>
        </svg>
        <h3 class="product-name is-blue">GLIDETRAY</h3>
        <p class="product-text">Lorem ipsum dolor sit amet,consectetur ipiscing elit. Nunc eget nunc vitae tellus luctu ullamcorp-er. consectetur adipiscing elit. unc eget nunc vitae tellus luctus ullamcorper.</p>
        <a class="button-solid" href="#">READ MORE</a>
      </article>
      <article class="product-card">
        <svg class="product-icon" width="112" height="112" viewBox="0 0 112 112" aria-hidden="true">
          <circle cx="56" cy="56" r="56" fill="#0d8ac6"/>
          <circle cx="56" cy="56" r="36" fill="none" stroke="#fff" stroke-width="3"/>
          <circle cx="56" cy="56" r="32" fill="#fff"/>
          <g fill="var(--brand-orange)">
            <circle cx="48" cy="58" r="10"/>
            <circle cx="65" cy="46" r="6.5"/>
            <circle cx="66" cy="67" r="6.5"/>
            <g stroke="var(--brand-orange)" stroke-width="4">
              <path d="M48 44v28M34 58h28M38 48l20 20M58 48l-20 20"/>
              <path d="M65 37v18M56 46h18M66 58v18M57 67h18"/>
            </g>
          </g>
          <g fill="#fff"><circle cx="48" cy="58" r="4"/><circle cx="65" cy="46" r="2.5"/><circle cx="66" cy="67" r="2.5"/></g>
        </svg>
        <h3 class="product-name is-teal">TUBEKEEPER <span class="accent">IV</span></h3>
        <p class="product-text">Lorem ipsum dolor sit amet,consectetur ipiscing elit. Nunc eget nunc vitae tellus luctu ullamcorp-er. consectetur adipiscing elit. unc eget nunc vitae tellus luctus ullamcorper.</p>
        <a class="button-solid" href="#">READ MORE</a>
      </article>
      <article class="product-card">
        <svg class="product-icon" width="112" height="112" viewBox="0 0 112 112" aria-hidden="true">
          <circle cx="56" cy="56" r="54" fill="#fff" stroke="var(--brand-orange)" stroke-width="4"/>
          <g fill="var(--brand-orange)">
            <path d="M72 34 C62 34 52 42 46 52 L58 64 C68 58 76 48 76 38 Z"/>
            <path d="M46 52 L36 52 L31 60 L42 60 Z"/>
            <path d="M58 64 L58 74 L50 79 L50 68 Z"/>
            <path d="M42 66 L46 70 L36 78 Z"/>
          </g>
          <circle cx="64" cy="46" r="4" fill="#fff"/>
        </svg>
        <h3 class="product-name is-orange">FASTPART</h3>
        <p class="product-text">Lorem ipsum dolor sit amet,consectetur ipiscing elit. Nunc eget nunc vitae tellus luctu ullamcorp-er. consectetur adipiscing elit. unc eget nunc vitae tellus luctus ullamcorper.</p>
        <a class="button-solid is-orange" href="#">READ MORE</a>
      </article>
    </div>
  </section>
</body>
</html>
```